" Empreiteira de mão de obra, que terceiriza a execução de projetos residências de médio e alto padrão, atuando a mais de 10 anos no mercado da construção civil. "

```html
<!DOCTYPE html>
<html lang="pt-BR">
<head>
<meta charset="utf-8">
<title>Fortiva – Flyer</title>
<link rel="stylesheet" href="https://fonts.googleapis.com/css2?family=Open+Sans:ital,wght@0,400;0,600;0,700;0,800;1,400;1,600;1,700;1,800&display=swap">
<style>
  :root{
    --green-dark:#1f6b32;
    --green:#2f8a3c;
    --green-mid:#4ea24a;
    --green-light:#8cc63f;
    --white:#ffffff;
    --page:#eef0ee;
    --photo-sky:#b9c7cf;
    --photo-house:#d8c46a;
    --photo-ground:#9b9686;
  }
  *{margin:0;padding:0;box-sizing:border-box}
  html,body{width:1200px;height:1200px;overflow:hidden;background:var(--page);font-family:"Open Sans",Arial,sans-serif}
  .flyer{position:absolute;left:210px;top:50px;width:780px;height:1100px;background:var(--white);overflow:hidden;box-shadow:0 6px 24px rgba(0,0,0,.12)}
  .flyer-shapes{position:absolute;inset:0}
  .brand{position:absolute;right:40px;top:440px;width:175px;text-align:center;color:var(--green)}
  .brand-row{display:flex;align-items:center;gap:8px;justify-content:center}
  .brand-dot{width:22px;height:22px;border-radius:50%;background:var(--green)}
  .brand-name{font-weight:800;font-size:30px;letter-spacing:1px;line-height:1}
  .brand-sub{font-size:12px;font-weight:600;margin-top:4px}
  .headline{position:absolute;left:40px;top:580px;width:620px;color:var(--white);font-style:italic;font-size:38px;line-height:1.2;text-align:center}
  .headline strong{font-weight:800}
  .contact{position:absolute;left:40px;top:770px;color:var(--white)}
  .contact-title{font-weight:800;font-size:24px;margin-bottom:16px}
  .contact-list{list-style:none}
  .contact-list li{display:flex;align-items:center;gap:12px;font-size:17px;margin-bottom:11px;line-height:1.25}
  .contact-list svg{width:20px;height:20px;flex:none}
  .offer{position:absolute;right:40px;top:845px;width:270px;text-align:right;color:var(--green);font-style:italic;font-size:28px;line-height:1.2}
  .offer strong{font-weight:800}
</style>
</head>
<body>
<main class="flyer">
  <svg class="flyer-shapes" viewBox="0 0 780 1100" width="780" height="1100">
    <defs>
      <linearGradient id="photoFill" x1="0" y1="0" x2="0" y2="1">
        <stop offset="0" stop-color="var(--photo-sky)"/>
        <stop offset=".55" stop-color="var(--photo-house)"/>
        <stop offset="1" stop-color="var(--photo-ground)"/>
      </linearGradient>
      <linearGradient id="bannerFill" x1="0" y1="0" x2="1" y2="0">
        <stop offset="0" stop-color="var(--green-dark)"/>
        <stop offset="1" stop-color="var(--green-mid)"/>
      </linearGradient>
      <linearGradient id="footFill" x1="0" y1="0" x2="1" y2="1">
        <stop offset="0" stop-color="var(--green-dark)"/>
        <stop offset="1" stop-color="var(--green)"/>
      </linearGradient>
    </defs>
    <polygon role="img" aria-label="Fotografia de uma casa de dois andares amarela com telhado escuro e jardim" points="0,0 780,0 780,120 470,560 0,560" fill="url(#photoFill)"/>
    <polygon points="0,0 190,0 0,240" fill="var(--green)"/>
    <polygon points="0,0 110,0 0,140" fill="var(--green-dark)"/>
    <polygon points="780,60 780,120 470,560 420,560" fill="var(--green-mid)"/>
    <polygon points="780,20 780,60 420,560 385,560" fill="var(--green-dark)"/>
    <polygon points="0,560 720,560 630,710 0,710" fill="url(#bannerFill)"/>
    <polygon points="140,715 200,715 170,745" fill="var(--green-light)"/>
    <polygon points="0,740 300,740 470,1100 0,1100" fill="url(#footFill)"/>
    <polygon points="300,740 330,740 500,1100 470,1100" fill="var(--green-light)"/>
    <polygon points="330,740 350,740 520,1100 500,1100" fill="var(--green-dark)"/>
    <polygon points="540,980 600,980 570,1010" fill="var(--green-light)"/>
  </svg>

  <div class="brand">
    <div class="brand-row"><span class="brand-dot"></span><span class="brand-name">FORTIVA</span></div>
    <div class="brand-sub">Construtora Ltda</div>
  </div>

  <h1 class="headline">Há mais de <strong>10 anos</strong> no mercado<br>de <strong>construção civil</strong></h1>

  <section class="contact">
    <h2 class="contact-title">Entre em contato já!</h2>
    <ul class="contact-list">
      <li><svg viewBox="0 0 24 24"><path fill="#fff" d="M6.6 10.8a15 15 0 0 0 6.6 6.6l2.2-2.2c.3-.3.7-.4 1-.2 1.1.4 2.3.6 3.6.6.6 0 1 .4 1 1V20c0 .6-.4 1-1 1A17 17 0 0 1 3 4c0-.6.4-1 1-1h3.5c.6 0 1 .4 1 1 0 1.3.2 2.5.6 3.6.1.3 0 .7-.2 1z"/></svg>(00) 0000-0000</li>
      <li><svg viewBox="0 0 24 24"><circle cx="12" cy="12" r="9" fill="none" stroke="#fff" stroke-width="2"/><path d="M3 12h18M12 3c3 3 3 15 0 18M12 3c-3 3-3 15 0 18" fill="none" stroke="#fff" stroke-width="1.6"/></svg>www.fortiva.com.br</li>
      <li><svg viewBox="0 0 24 24"><rect x="3" y="6" width="18" height="12" rx="1.5" fill="none" stroke="#fff" stroke-width="2"/><path d="M3 7l9 6 9-6" fill="none" stroke="#fff" stroke-width="2"/></svg>contato@fortiva.com.br</li>
      <li><svg viewBox="0 0 24 24"><path fill="#fff" d="M12 2a7 7 0 0 0-7 7c0 5 7 13 7 13s7-8 7-13a7 7 0 0 0-7-7zm0 9.5A2.5 2.5 0 1 1 12 6.5a2.5 2.5 0 0 1 0 5z"/></svg><span>Endereço completo, nº 123<br>Cidade - Estado - UF</span></li>
    </ul>
  </section>

  <p class="offer">Venda de <strong>mão de obra</strong> com <strong>gestão de projetos</strong>!</p>
</main>
</body>
</html>
```